Pebble Ledger WEB application

We need a small webdesign for a WEB-Application. Functionality will be provided by our developers. All we need are templates with HTML5, CSS and Java functionality for the "animated" parts. As well as some images and logos .
See attached Powerpoint. Please ignore last slide.
Design should be state of the art material design as know from Quorvix or Zelpad latest OS versions
In the end will be fluid design (fitting automatically to actual screen size) but template should base on 540 x 960

Target Market(s)

UK Mobile Market

Number of Pages Required

5+ page

Font styles to use
Sans Serif

Requirements
Must have
• next to requierements in Powerpoint we need animations as stated in PP (progress animation).
Nice to have
• All textfiles should be in a XML file to be easily translated to other languages.Can be done by our developers as well

```html
<!DOCTYPE html>
<html lang="en">
<head>
<meta charset="utf-8">
<title>Battery optimization</title>
<link rel="stylesheet" href="https://fonts.googleapis.com/css2?family=Cabin+Condensed:wght@400;500;600&display=swap">
<style>
  :root {
    --paper-light: #f3e6c4;
    --paper-mid: #e9d6a8;
    --paper-edge: #c9ad78;
    --ink: #141210;
    --battery-red: #c8221d;
    --battery-red-dark: #8e1512;
  }
  * { box-sizing: border-box; margin: 0; padding: 0; }
  html, body { width: 675px; height: 1200px; overflow: hidden; }
  body {
    font-family: "Cabin Condensed", "Arial Narrow", sans-serif;
    color: var(--ink);
    background: radial-gradient(ellipse at 50% 45%, var(--paper-light) 0%, var(--paper-mid) 60%, var(--paper-edge) 100%);
  }
  .screen { position: relative; width: 675px; height: 1200px; }

  .headline {
    position: absolute;
    top: 82px; left: 0; width: 675px;
    padding-left: 40px;
    text-align: center;
    font-weight: 500;
    font-size: 76px;
    line-height: 88px;
    letter-spacing: 1px;
  }

  .score { position: absolute; top: 260px; left: 168px; display: flex; align-items: center; gap: 32px; }
  .score-value { font-size: 74px; font-weight: 500; letter-spacing: 2px; }
  .battery-icon { width: 154px; height: 88px; }

  .check-list { position: absolute; top: 422px; left: 68px; list-style: none; }
  .check-item { display: flex; align-items: center; height: 62px; }
  .check-label { font-size: 52px; line-height: 1; white-space: nowrap; letter-spacing: 0.5px; }
  .check-bar { display: block; width: 432px; height: 42px; display: flex; }
  .check-row { display: flex; align-items: center; width: 432px; gap: 4px; }
  .check-row .bar { flex: 1; height: 42px; background: var(--ink); }
  .tick { width: 46px; height: 42px; margin-left: 30px; }

  .cta {
    position: absolute;
    top: 936px; left: 142px;
    width: 387px; height: 54px;
    border: 3px solid var(--ink);
    display: flex; align-items: center; justify-content: center;
    font-size: 22px; font-weight: 600; letter-spacing: 1px;
    background: transparent;
    color: var(--ink);
    font-family: inherit;
  }
</style>
</head>
<body>
<main class="screen">
  <h1 class="headline">Overall Battery<br>optimization:</h1>

  <div class="score">
    <span class="score-value">26%</span>
    <svg class="battery-icon" viewBox="0 0 154 88" aria-hidden="true">
      <rect x="4" y="4" width="132" height="80" rx="8" fill="var(--battery-red)" stroke="var(--ink)" stroke-width="5"/>
      <rect x="10" y="10" width="120" height="14" rx="4" fill="var(--battery-red-dark)" opacity="0.5"/>
      <rect x="136" y="26" width="14" height="36" rx="3" fill="var(--ink)"/>
    </svg>
  </div>

  <ul class="check-list">
    <li class="check-item"><span class="check-row"><span class="check-label">System</span><span class="bar"></span></span><svg class="tick" viewBox="0 0 46 42" aria-hidden="true"><path d="M4 24 L16 36 L42 4" fill="none" stroke="var(--ink)" stroke-width="7" stroke-linecap="round" stroke-linejoin="round"/></svg></li>
    <li class="check-item"><span class="check-row"><span class="check-label">Memory</span><span class="bar"></span></span><svg class="tick" viewBox="0 0 46 42" aria-hidden="true"><path d="M4 24 L16 36 L42 4" fill="none" stroke="var(--ink)" stroke-width="7" stroke-linecap="round" stroke-linejoin="round"/></svg></li>
    <li class="check-item"><span class="check-row"><span class="check-label">Accounts</span><span class="bar"></span></span><svg class="tick" viewBox="0 0 46 42" aria-hidden="true"><path d="M4 24 L16 36 L42 4" fill="none" stroke="var(--ink)" stroke-width="7" stroke-linecap="round" stroke-linejoin="round"/></svg></li>
    <li class="check-item"><span class="check-row"><span class="check-label">Sync Processes</span><span class="bar"></span></span><svg class="tick" viewBox="0 0 46 42" aria-hidden="true"><path d="M4 24 L16 36 L42 4" fill="none" stroke="var(--ink)" stroke-width="7" stroke-linecap="round" stroke-linejoin="round"/></svg></li>
    <li class="check-item"><span class="check-row"><span class="check-label">Localization</span><span class="bar"></span></span><svg class="tick" viewBox="0 0 46 42" aria-hidden="true"><path d="M4 24 L16 36 L42 4" fill="none" stroke="var(--ink)" stroke-width="7" stroke-linecap="round" stroke-linejoin="round"/></svg></li>
    <li class="check-item"><span class="check-row"><span class="check-label">Bluetooth</span><span class="bar"></span></span><svg class="tick" viewBox="0 0 46 42" aria-hidden="true"><path d="M4 24 L16 36 L42 4" fill="none" stroke="var(--ink)" stroke-width="7" stroke-linecap="round" stroke-linejoin="round"/></svg></li>
    <li class="check-item"><span class="check-row"><span class="check-label">Apps</span><span class="bar"></span></span><svg class="tick" viewBox="0 0 46 42" aria-hidden="true"><path d="M4 24 L16 36 L42 4" fill="none" stroke="var(--ink)" stroke-width="7" stroke-linecap="round" stroke-linejoin="round"/></svg></li>
  </ul>

  <button class="cta" type="button">START FREE OPTIMIZATION NOW</button>
</main>
</body>
</html>
```